Website design for a construction company

The logo and the copies of all the 3 pages are attached below. I don't have a preference in colors but I would ideally like to use the colors on my logo, dark teal (secondary) and copper (primary).

Company Name: Torvin Group

Location: London, UK

Business Overview:

Torvin Group is a comprehensive construction company based in London, specializing in a wide range of construction services. We cater to various sectors, providing services including electrical work, painting and decorating, plastering, plumbing, carpentry, kitchen and bathroom installations, loft conversions, and extensions. Our team is known for its skilled craftsmanship, attention to detail, and commitment to quality.

What "TORVIN" stands for:

Our company name, 'TORVIN', is derived from Hephaestus, the ancient Greek god of craftsmen, blacksmiths, artisans, sculptors, metals, metallurgy, fire, and volcanoes. Hephaestus was renowned in mythology for his incredible skill in crafting and creating, making him the patron of all craftsmen and artisans. His name is synonymous with the mastery of artisanship and the creation of wondrous, enduring works.

In choosing 'TORVIN' as our name, we embody the spirit and skills of Hephaestus. It reflects our commitment to craftsmanship, excellence, and durability in the field of construction. Just as Hephaestus was known for his meticulous work, precision, and innovative creations, our company strives to uphold these qualities in every project we undertake.

Our name is a constant reminder of our dedication to quality, innovation, and the art of building. It symbolizes our endeavor to achieve the highest standards in construction, much like Hephaestus did in his timeless creations. In essence, 'TORVIN' is not just our name; it's a representation of our ethos and the high standards we set for ourselves in the construction industry.

Target Audience:

Our primary audience includes homeowners, real estate developers, and commercial clients in London seeking reliable, high-quality construction services.

Unique Selling Points:

Diverse Range of Services: Offering a one-stop solution for all construction needs.

Certified and Experienced: Professional team with a strong focus on delivering certified and compliant work, particularly in electrical services.

Client-Centric Approach: Emphasizing client satisfaction, we tailor our services to meet the unique needs and visions of our clients.

Quality and Reliability: Commitment to high-quality materials, skilled workmanship, and delivering projects on time and within budget.

Website Requirements:

Clean, professional design reflecting the quality and reliability of our services.

User-friendly navigation to easily access information about our services, portfolio, company background, and contact details.

Portfolio section showcasing our past projects with placeholders for images and descriptions.

Integration of a contact form, map for our location, and links to our social media accounts.

Mobile-responsive design to ensure accessibility across various devices.

Purpose of the Website:
The website aims to:

Establish an online presence and credibility in the construction industry.

Provide an informative resource about our services and past projects to potential clients.

Facilitate easy communication and inquiries through an integrated contact system.

Tone and Style:

Professional, informative, and welcoming. The website should convey trustworthiness and expertise in the construction field.

homeowners, real estate developers, and commercial clients

Construction

3 page

```html
<!DOCTYPE html>
<html lang="en">
<head>
<meta charset="utf-8">
<title>Torvin Group – Construction in London</title>
<link href="https://fonts.googleapis.com/css2?family=Lato:wght@400;700;900&display=swap" rel="stylesheet">
<style>
:root{
  --copper:#a87b3f;
  --copper-dark:#8f6530;
  --teal:#138476;
  --grey-bg:#ececec;
  --ink:#1d1d1d;
  --line:#b99a6a;
  --white:#ffffff;
}
*{box-sizing:border-box;margin:0;padding:0}
html,body{width:1200px;height:3217px;overflow:hidden;background:var(--white)}
body{font-family:'Lato',sans-serif;color:var(--ink)}
.page{position:relative;width:1200px;height:3217px;overflow:hidden}
.abs{position:absolute}
.photo{position:absolute}

/* header */
.site-header{position:absolute;left:0;top:0;width:1200px;height:69px;background:linear-gradient(90deg,#a3793f,#b08a52 50%,#a67c44);z-index:3}
.brand{position:absolute;left:249px;top:19px;display:flex;align-items:center;gap:10px;color:var(--white);font-size:26px;font-weight:400;letter-spacing:1px}
.brand-mark{width:26px;height:26px;background:var(--white)}
.main-nav{position:absolute;top:30px;left:0;font-size:11.5px;color:var(--white)}
.main-nav span{position:absolute;white-space:nowrap}

/* hero */
.hero{position:absolute;left:0;top:69px;width:1200px;height:531px;
  background:
    linear-gradient(90deg,rgba(12,118,104,.92) 0%,rgba(20,120,100,.75) 22%,rgba(20,110,90,.25) 42%,rgba(0,0,0,0) 55%),
    radial-gradient(ellipse 340px 150px at 770px 250px,#5a4332 0%,#6e5240 45%,rgba(110,82,64,0) 100%),
    radial-gradient(ellipse 260px 70px at 760px 150px,#d9d2c4 0%,rgba(217,210,196,0) 100%),
    radial-gradient(ellipse 380px 120px at 1050px 470px,#b69462 0%,rgba(182,148,98,0) 100%),
    linear-gradient(180deg,#c9ccce 0%,#b9bdb9 10%,#7f8d63 24%,#5f7a3e 40%,#6b7f3b 60%,#74813e 80%,#8c8a4a 100%)}
.hero-copy{position:absolute;left:249px;top:176px;color:var(--white)}
.hero-title{font-size:29px;font-weight:900;line-height:31px;letter-spacing:.3px;text-shadow:0 2px 3px rgba(0,0,0,.35)}
.hero-sub{margin-top:12px;font-size:15.5px;line-height:17px;font-weight:400}
.hero-text{margin-top:14px;width:262px;font-size:11.3px;line-height:16.3px}

/* about */
.about-bar{left:250px;top:701px;width:260px;height:224px;background:var(--teal)}
.about-bar-inner{left:266px;top:701px;width:244px;height:208px;background:var(--white)}
.about-photo{left:270px;top:654px;width:376px;height:250px;
  background:
    radial-gradient(ellipse 70px 90px at 115px 70px,#8a7d6c 0%,rgba(138,125,108,0) 100%),
    radial-gradient(ellipse 150px 45px at 190px 145px,#5d6672 0%,rgba(93,102,114,0) 100%),
    radial-gradient(ellipse 160px 50px at 180px 190px,#e6e7e9 0%,#b8c3cc 50%,rgba(184,195,204,0) 100%),
    radial-gradient(ellipse 120px 25px at 160px 228px,#2c5fa8 0%,rgba(44,95,168,0) 100%),
    linear-gradient(180deg,#dfe1e5 0%,#cfd2d7 40%,#9ea3a8 62%,#5a5752 78%,#3f3c39 100%)}
.about-title{left:677px;top:717px;font-size:22px;font-weight:900;color:var(--teal)}
.about-text{left:677px;top:752px;width:278px;font-size:11px;line-height:14px}

/* why */
.why{left:0;top:980px;width:1200px;height:576px;background:var(--grey-bg);overflow:hidden}
.why-lines{position:absolute;left:0;top:1255px}
.sec-title{position:absolute;left:0;width:1200px;text-align:center;font-size:22px;font-weight:900;color:var(--copper)}
.why-photo-1{left:249px;top:1062px;width:208px;height:207px;
  background:
    radial-gradient(ellipse 38px 20px at 105px 30px,#e2541e 0%,rgba(226,84,30,0) 100%),
    radial-gradient(ellipse 30px 30px at 105px 58px,#d9a98a 0%,rgba(217,169,138,0) 100%),
    radial-gradient(ellipse 60px 70px at 110px 150px,#f07a1c 0%,#e86c16 50%,rgba(232,108,22,0) 100%),
    radial-gradient(ellipse 75px 100px at 110px 140px,#2a2433 0%,rgba(42,36,51,0) 100%),
    linear-gradient(90deg,#7e8e9e 0%,#b46a45 20%,#8a98a8 45%,#b96f46 75%,#7d8c9c 100%)}
.why-photo-2{left:744px;top:1319px;width:208px;height:207px;
  background:
    radial-gradient(circle at 72px 70px,#b7f0ff 0%,#3fa7d6 14%,rgba(63,167,214,0) 36%),
    radial-gradient(ellipse 45px 40px at 60px 150px,#e9b79a 0%,rgba(233,183,154,0) 100%),
    radial-gradient(ellipse 60px 100px at 170px 90px,#2a2d33 0%,rgba(42,45,51,0) 100%),
    linear-gradient(135deg,#0e1e2d,#1f3d58 45%,#0c1620)}
.frame-r{left:951px;top:1115px;width:1px;height:100px;background:var(--line)}
.frame-b{left:496px;top:1213px;width:456px;height:1px;background:var(--line)}
.frame-l2{left:250px;top:1359px;width:1px;height:143px;background:var(--line)}
.frame-b2{left:250px;top:1501px;width:450px;height:1px;background:var(--line)}
.point-title{font-size:15px;font-weight:900;color:var(--teal)}
.point-text{margin-top:6px;font-size:10.6px;line-height:14px}
.point-sub{margin-top:18px;font-size:15px;font-weight:700;color:#111}

/* services */
.services-intro{left:330px;top:1620px;width:540px;text-align:center;font-size:10.8px;line-height:14px}
.svc{position:absolute;width:202px}
.svc-frame{position:absolute;left:-5px;top:-5px;width:202px;height:201px;border:1px solid #d9c4a6;border-right:none;border-bottom:none}
.svc-frame::after{content:"";position:absolute;right:-1px;top:0;width:1px;height:5px;background:#d9c4a6}
.svc-img{position:relative;width:202px;height:201px}
.svc-name{margin-top:23px;text-align:center;font-size:11px;font-weight:900;color:var(--teal);letter-spacing:.2px;line-height:13px}

.ph-elec{background:
  radial-gradient(ellipse 40px 24px at 130px 35px,#2f7fc8 0%,rgba(47,127,200,0) 100%),
  radial-gradient(ellipse 55px 80px at 150px 120px,#d85a28 0%,rgba(216,90,40,0) 100%),
  radial-gradient(ellipse 30px 30px at 100px 125px,#e3c03a 0%,rgba(227,192,58,0) 100%),
  linear-gradient(90deg,#d5d8db 0%,#9aa2aa 25%,#5c6570 50%,#7a6a60 100%)}
.ph-paint{background:
  radial-gradient(ellipse 25px 45px at 110px 105px,#3c4a5e 0%,rgba(60,74,94,0) 100%),
  radial-gradient(ellipse 90px 30px at 100px 185px,#2f343a 0%,rgba(47,52,58,0) 100%),
  linear-gradient(90deg,#f2f2f2 0%,#e4e6e8 40%,#8fb9d6 70%,#3a9bd3 100%)}
.ph-plaster{background:
  radial-gradient(ellipse 40px 70px at 95px 100px,#2b2b2d 0%,rgba(43,43,45,0) 100%),
  radial-gradient(ellipse 20px 60px at 145px 70px,#efede8 0%,rgba(239,237,232,0) 100%),
  linear-gradient(135deg,#dcd8cf,#c9c3b8 60%,#b2ab9f)}
.ph-plumb{background:
  radial-gradient(ellipse 45px 70px at 150px 110px,#27375a 0%,rgba(39,55,90,0) 100%),
  radial-gradient(ellipse 30px 60px at 40px 90px,#2d2d2d 0%,rgba(45,45,45,0) 100%),
  linear-gradient(180deg,#f4f4f4 0%,#e8e8e8 45%,#d3d5d8 100%)}
.ph-carp{background:
  radial-gradient(ellipse 60px 90px at 150px 90px,#6f6d2e 0%,#b9a03c 40%,rgba(185,160,60,0) 100%),
  radial-gradient(ellipse 60px 90px at 55px 95px,#c98a45 0%,rgba(201,138,69,0) 100%),
  linear-gradient(135deg,#ddd5c8,#c5b8a4 60%,#8d7656)}
.ph-kitchen{background:
  radial-gradient(ellipse 50px 90px at 155px 100px,#7a4f33 0%,rgba(122,79,51,0) 100%),
  radial-gradient(ellipse 90px 22px at 80px 175px,#2c2c2c 0%,rgba(44,44,44,0) 100%),
  linear-gradient(135deg,#fbfbfb,#e6e6e6 55%,#cfcfcf)}
.ph-loft{background:
  radial-gradient(ellipse 55px 25px at 100px 150px,#b8743a 0%,rgba(184,116,58,0) 100%),
  radial-gradient(ellipse 100px 40px at 100px 30px,#cdd0cc 0%,rgba(205,208,204,0) 100%),
  linear-gradient(180deg,#8a8b84 0%,#5b4b3c 45%,#6b4126 75%,#3b2416 100%)}
.ph-ext{background:
  radial-gradient(ellipse 18px 40px at 150px 120px,#c84b55 0%,rgba(200,75,85,0) 100%),
  radial-gradient(ellipse 80px 30px at 150px 185px,#b27a40 0%,rgba(178,122,64,0) 100%),
  linear-gradient(160deg,#cfd2d8 0%,#b9bcc3 15%,#23262b 30%,#30343a 65%,#8f5b2e 100%)}

/* testimonials */
.testi{left:0;top:2221px;width:1200px;height:324px;background:var(--grey-bg);overflow:hidden}
.testi-lines{position:absolute;left:1050px;top:2390px}
.testi-photo{left:249px;top:2299px;width:342px;height:200px;
  background:
    radial-gradient(ellipse 40px 80px at 320px 60px,#4f7a3a 0%,rgba(79,122,58,0) 100%),
    radial-gradient(ellipse 30px 60px at 25px 70px,#4f7a3a 0%,rgba(79,122,58,0) 100%),
    radial-gradient(ellipse 130px 75px at 180px 125px,#fbfbf9 0%,#e8e6e0 60%,rgba(232,230,224,0) 100%),
    radial-gradient(ellipse 60px 20px at 200px 120px,#8b6a48 0%,rgba(139,106,72,0) 100%),
    linear-gradient(180deg,#84b4e0 0%,#b9d4ec 35%,#e3ebf0 55%,#c9c6bb 85%,#9b9685 100%)}
.testi-card{left:609px;top:2299px;width:343px;height:200px;background:var(--white);box-shadow:0 1px 6px rgba(0,0,0,.12);padding:46px 20px 0 16px}
.view-all{font-size:13.5px;font-weight:700;color:var(--copper)}
.dots{position:absolute;right:20px;top:51px;display:flex;gap:3px}
.dots i{width:5px;height:5px;background:#b4b4b4;display:block}
.dots i.on{width:7px;height:7px;margin-top:-1px;background:var(--copper)}
.testi-text{margin-top:22px;font-size:10.6px;line-height:14px}
.testi-name{font-size:10.6px;font-weight:700;color:var(--teal);margin-top:2px}

/* contact */
.contact-intro{left:340px;top:2606px;width:520px;text-align:center;font-size:10.8px;line-height:14px}
.contact-box{left:249px;top:2664px;width:703px;height:352px;background:var(--white);box-shadow:0 1px 7px rgba(0,0,0,.14)}
.form-title{left:275px;top:2691px;font-size:14.5px;font-weight:700;color:var(--copper)}
.field{position:absolute;left:275px;width:363px;border-bottom:1px solid #8a8a8a;font-size:11px;padding-bottom:3px}
.btn{position:absolute;height:32px;background:var(--copper);color:var(--white);font-size:11px;font-weight:700;display:flex;align-items:center;justify-content:center;letter-spacing:.3px}
.info-panel{left:668px;top:2664px;width:284px;height:216px;background:var(--copper)}
.info-title{left:694px;top:2691px;font-size:14.5px;font-weight:700;color:var(--white)}
.info-row{position:absolute;left:694px;display:flex;gap:16px;color:var(--white);font-size:10.6px;line-height:13px;align-items:flex-start}
.social{position:absolute;top:2843px;width:22px;height:22px;border:1.5px solid var(--white);border-radius:50%}
.map{left:668px;top:2880px;width:284px;height:136px;
  background:
    radial-gradient(ellipse 90px 14px at 200px 60px,#9fb3d6 0%,rgba(159,179,214,0) 100%),
    radial-gradient(ellipse 14px 70px at 120px 50px,#9fb3d6 0%,rgba(159,179,214,0) 100%),
    radial-gradient(ellipse 60px 30px at 60px 30px,#f3dcc0 0%,rgba(243,220,192,0) 100%),
    linear-gradient(135deg,#eef0f2,#e2e7ec 50%,#ece6da)}

/* footer */
.site-footer{left:0;top:3047px;width:1200px;height:125px;background:var(--grey-bg)}
.foot-brand{position:absolute;left:0;width:1200px;top:3072px;display:flex;justify-content:center;align-items:center;gap:10px;font-size:30px;color:#333;letter-spacing:1px}
.foot-brand .brand-mark{width:28px;height:28px;background:var(--copper)}
.quick{left:0;width:1200px;top:3118px;text-align:center;font-size:14px;font-weight:900;color:var(--teal)}
.quick-line{left:563px;top:3136px;width:74px;height:1px;background:var(--teal)}
.foot-nav{left:0;top:3143px;width:1200px;font-size:11px}
.foot-nav span{position:absolute;white-space:nowrap}
.bottom-bar{left:0;top:3172px;width:1200px;height:45px;background:linear-gradient(90deg,#a27a3e,#a48046 60%,#168a78)}
.copyright{left:249px;top:3190px;font-size:10.6px;color:var(--white)}
</style>
</head>
<body>
<div class="page">

  <header class="site-header">
    <div class="brand"><span class="brand-mark"></span>TORVIN</div>
    <nav class="main-nav">
      <span style="left:612px">Home</span>
      <span style="left:679px">About Us</span>
      <span style="left:756px">Services</span>
      <span style="left:831px">Projects</span>
      <span style="left:898px">Contact Us</span>
    </nav>
  </header>

  <section class="hero" role="img" aria-label="Modern two-storey stone-clad house on a hillside with green lawn and winding dirt path">
    <div class="hero-copy">
      <h1 class="hero-title">BUILDING YOUR<br>DREAMS INTO REALITY</h1>
      <p class="hero-sub">EXPERT CRAFTSMANSHIP MEETS UNMATCHED<br>RELIABILITY IN THE HEART OF LONDON</p>
      <p class="hero-text">Welcome to Torvin Group – Where Construction Meets Excellence. Based in London, we are committed to transforming your spaces into exceptional places. Our team is dedicated to delivering the highest quality in every project, attending to every detail with precision and care.</p>
    </div>
  </section>

  <section>
    <div class="abs about-bar"></div>
    <div class="abs about-bar-inner"></div>
    <div class="photo about-photo" role="img" aria-label="Single-storey house under construction with scaffolding and a bare tree behind"></div>
    <h2 class="abs about-title">ABOUT US</h2>
    <p class="abs about-text">At Torvin Group, our journey began with a vision – to create a construction company that stands apart in its commitment to excellence, reliability, and customer satisfaction. Based in the heart of London, we've grown from a small team of enthusiastic builders to a full-fledged construction company renowned for quality and integrity.</p>
  </section>

  <section>
    <div class="abs why"></div>
    <svg class="why-lines" width="200" height="301" viewBox="0 0 200 301" aria-hidden="true">
      <path d="M0 40 L180 301" stroke="#dcdcdc" stroke-width="14" fill="none"/>
      <path d="M0 110 L130 301" stroke="#e2e2e2" stroke-width="10" fill="none"/>
    </svg>
    <h2 class="sec-title" style="top:1003px">WHY CHOOSE US</h2>
    <div class="photo why-photo-1" role="img" aria-label="Smiling builder in hard hat and high-visibility vest in front of a building"></div>
    <div class="abs frame-r"></div>
    <div class="abs frame-b"></div>
    <div class="abs" style="left:488px;top:1123px;width:420px">
      <h3 class="point-title">OUR EXPERTISE :</h3>
      <p class="point-text">Leveraging over 10 years of experience, Torvin Group stands as a beacon of excellence in the construction industry. We handle each project, big or small, with unmatched professionalism and skill.</p>
    </div>
    <div class="abs frame-l2"></div>
    <div class="abs frame-b2"></div>
    <div class="abs" style="left:287px;top:1356px;width:420px">
      <h3 class="point-title">QUALITY ASSURANCE :</h3>
      <p class="point-text">Quality is not just a promise, but a practice. Meticulous attention to detail ensures flawless finishes and durable structures, bringing long-lasting satisfaction to our clients.</p>
      <h4 class="point-sub">Certified Excellence:</h4>
      <p class="point-text" style="margin-top:4px">Your safety and satisfaction are our top priorities. We provide electrical certificates and adhere to the highest industry standards, offering peace of mind in every service.</p>
    </div>
    <div class="photo why-photo-2" role="img" aria-label="Businessman touching a glowing standards gear icon"></div>
  </section>

  <section>
    <h2 class="sec-title" style="top:1581px">SERVICES</h2>
    <p class="abs services-intro">Our Services – Tailored to Your Needs. Discover how we can bring your vision to life, covering every aspect of construction from the initial design to the final touches.</p>

    <div class="svc" style="left:100px;top:1696px"><div class="svc-frame"></div><div class="svc-img ph-elec" role="img" aria-label="Electrician testing a fuse board"></div><div class="svc-name">ELECTRICAL WORK</div></div>
    <div class="svc" style="left:368px;top:1696px"><div class="svc-frame"></div><div class="svc-img ph-paint" role="img" aria-label="Decorator painting a wall blue"></div><div class="svc-name">PAINTING AND DECORATING</div></div>
    <div class="svc" style="left:636px;top:1696px"><div class="svc-frame"></div><div class="svc-img ph-plaster" role="img" aria-label="Plasterer smoothing a wall"></div><div class="svc-name">PLASTERING</div></div>
    <div class="svc" style="left:903px;top:1696px"><div class="svc-frame"></div><div class="svc-img ph-plumb" role="img" aria-label="Plumber fitting a kitchen sink"></div><div class="svc-name">PLUMBING</div></div>

    <div class="svc" style="left:100px;top:1951px"><div class="svc-frame"></div><div class="svc-img ph-carp" role="img" aria-label="Carpenter sanding a wooden frame"></div><div class="svc-name">CARPENTRY</div></div>
    <div class="svc" style="left:368px;top:1951px"><div class="svc-frame"></div><div class="svc-img ph-kitchen" role="img" aria-label="Fitter installing kitchen wall cabinets"></div><div class="svc-name">KITCHEN AND BATHROOM<br>INSTALLATIONS</div></div>
    <div class="svc" style="left:636px;top:1951px"><div class="svc-frame"></div><div class="svc-img ph-loft" role="img" aria-label="Loft conversion with wooden floors and sofa"></div><div class="svc-name">LOFT CONVERSIONS</div></div>
    <div class="svc" style="left:903px;top:1951px"><div class="svc-frame"></div><div class="svc-img ph-ext" role="img" aria-label="Workers on a dark metal roof extension"></div><div class="svc-name">EXTENSIONS</div></div>
  </section>

  <section>
    <div class="abs testi"></div>
    <svg class="testi-lines" width="150" height="155" viewBox="0 0 150 155" aria-hidden="true">
      <path d="M150 0 L40 155" stroke="#dedede" stroke-width="12" fill="none"/>
      <path d="M150 60 L100 155" stroke="#e3e3e3" stroke-width="9" fill="none"/>
    </svg>
    <h2 class="sec-title" style="top:2250px">TESTIMONIALS</h2>
    <div class="photo testi-photo" role="img" aria-label="White modern villa with balconies among palm trees"></div>
    <div class="abs testi-card">
      <div class="view-all">VIEW ALL</div>
      <div class="dots"><i></i><i></i><i class="on"></i><i></i><i></i></div>
      <p class="testi-text">Hear from Our Satisfied Clients. Our commitment to excellence has earned us the trust of numerous homeowners and businesses in London. Read their stories and understand the Torvin Group difference.</p>
      <p class="testi-name">Marla &amp; Dean Hollis</p>
    </div>
  </section>

  <section>
    <h2 class="sec-title" style="top:2567px">CONTACT US</h2>
    <p class="abs contact-intro">Ready to Start Your Project? Contact us today for a consultation and embark on the journey to turn your construction dreams into a stunning reality.</p>
    <div class="abs contact-box"></div>
    <h3 class="abs form-title">INQUIRE ABOUT SERVICES</h3>
    <div class="field" style="top:2735px">Name</div>
    <div class="field" style="top:2778px">Email</div>
    <div class="field" style="top:2820px">Phone</div>
    <div class="field" style="top:2863px">Message</div>
    <div class="abs" style="left:275px;top:2930px;width:363px;height:1px;background:#8a8a8a"></div>
    <div class="btn" style="left:276px;top:2963px;width:107px">SEND MESSAGE</div>

    <div class="abs info-panel"></div>
    <h3 class="abs info-title">CONTACT INFO</h3>
    <div class="info-row" style="top:2732px">
      <svg width="16" height="16" viewBox="0 0 16 16"><circle cx="8" cy="8" r="7" fill="none" stroke="#fff" stroke-width="1.3"/><rect x="4.5" y="5.5" width="7" height="5" fill="#fff"/></svg>
      <span>info@torvingroup.co.uk</span></div>
    <div class="info-row" style="top:2761px">
      <svg width="16" height="16" viewBox="0 0 16 16"><circle cx="8" cy="8" r="7" fill="none" stroke="#fff" stroke-width="1.3"/><path d="M5.5 4.5c-.8.8-.6 2.6 1.3 4.6s3.6 2.2 4.4 1.3l-1.3-1.3-1 .6-2-2 .6-1z" fill="#fff"/></svg>
      <span>+ 44 20 7946 0321</span></div>
    <div class="info-row" style="top:2790px">
      <svg width="16" height="16" viewBox="0 0 16 16"><circle cx="8" cy="8" r="7" fill="none" stroke="#fff" stroke-width="1.3"/><path d="M8 3.8a2.7 2.7 0 0 0-2.7 2.7C5.3 8.6 8 12 8 12s2.7-3.4 2.7-5.5A2.7 2.7 0 0 0 8 3.8zm0 3.8a1.1 1.1 0 1 1 0-2.2 1.1 1.1 0 0 1 0 2.2z" fill="#fff"/></svg>
      <span>14 Fenwick Street<br>EC2 4RT, London, UK</span></div>
    <span class="social" style="left:696px"></span>
    <span class="social" style="left:731px"></span>
    <span class="social" style="left:765px"></span>
    <span class="social" style="left:800px"></span>
    <div class="photo map" role="img" aria-label="Street map of the office location in London"></div>
    <div class="btn" style="left:694px;top:2963px;width:106px">VIEW MAP</div>
  </section>

  <footer>
    <div class="abs site-footer"></div>
    <div class="foot-brand"><span class="brand-mark"></span>TORVIN</div>
    <div class="abs quick">Quick links</div>
    <div class="abs quick-line"></div>
    <nav class="abs foot-nav">
      <span style="left:452px">Home</span>
      <span style="left:508px">About Us</span>
      <span style="left:574px">Services</span>
      <span style="left:638px">Projects</span>
      <span style="left:695px">Contact Us</span>
    </nav>
    <div class="abs bottom-bar"></div>
    <p class="abs copyright">© 2024 <strong>Torvin Group.</strong> All Rights Reserved.</p>
  </footer>

</div>
</body>
</html>
```